Real Estate Brokerage Stationery Designs

I am looking to have presentation folders with business card slots on both sides along with pockets on both sides. I've attached logos, website colors along with current business card designs.

I am looking for envelope designs both big and small. Possibly new business card designs, notepad templates for big and small notepads. Letterhead designs. Pop socket designs. Realtors name badge designs.

www.brightkeelhomes.example

```html
<!DOCTYPE html>
<html lang="en">
<head>
<meta charset="utf-8">
<title>Brightkeel Homes Stationery Set</title>
<link href="https://fonts.googleapis.com/css2?family=Lato:wght@400;700&family=Great+Vibes&display=swap" rel="stylesheet">
<style>
:root{
  --backdrop:#e8e0d4;
  --paper:#ffffff;
  --grey:#b1b0b5;
  --grey-dark:#a4a3a8;
  --blue:#0b4da2;
  --ink:#1d1d1f;
  --muted:#8a8a8f;
  --shadow:0 6px 6px -3px rgba(0,0,0,.25);
}
*{box-sizing:border-box;margin:0;padding:0}
html,body{width:1200px;height:1200px;overflow:hidden}
body{background:var(--backdrop);font-family:'Lato',sans-serif;position:relative;color:var(--ink)}
.sheet{position:absolute;background:var(--paper);box-shadow:var(--shadow)}
.base-band{position:absolute;left:0;right:0;bottom:0;height:3px;background:var(--grey)}
.base-band::after{content:"";position:absolute;right:0;top:0;bottom:0;width:47%;background:var(--blue)}
.brand{position:absolute;display:flex;align-items:center;gap:.35em;font-weight:700;color:var(--ink);white-space:nowrap}
.brand-mark{width:.8em;height:.8em;background:var(--blue)}
.brand.on-grey{color:#fff}
.brand.on-grey .brand-mark{background:#fff}
.contact{position:absolute;list-style:none;color:var(--muted);line-height:1.45}
.contact li{display:flex;align-items:center;gap:.5em}
.contact svg{width:.9em;height:.9em;fill:var(--blue);flex:none}
.contact .gap{margin-top:.6em}
.contact.light{color:#e9e9ec}
.contact.light svg{fill:#e9e9ec}

/* folder */
.folder-outside{left:117px;top:47px;width:413px;height:290px}
.folder-spine{position:absolute;left:0;top:0;width:206px;height:100%;background:var(--grey)}
.folder-inside{left:117px;top:371px;width:413px;height:292px}
.folder-pocket{position:absolute;left:0;top:0;width:100%;height:100%}

/* envelopes */
.envelope{position:absolute}
.envelope svg.body{position:absolute;inset:0;width:100%;height:100%;overflow:visible}

/* business card */
.card-front{left:590px;top:261px;width:143px;height:81px;background:var(--grey)}
.card-back{left:590px;top:348px;width:143px;height:81px}
.card-name{position:absolute;left:14px;top:16px;font-size:5px;font-weight:700;color:var(--blue)}
.card-role{position:absolute;left:14px;top:22px;font-size:3px;color:var(--muted)}

/* letters */
.letter-tall{left:782px;top:245px;width:297px;height:420px}
.letter{left:167px;top:723px;width:280px;height:396px}
.letter-body{position:absolute;left:18px;right:17px;top:117px;font-size:4.2px;color:var(--muted);line-height:1.8;text-align:justify}
.letter-body p{margin-bottom:5px}
.letter-head{display:flex;justify-content:space-between;margin-bottom:10px;text-align:left}
.letter-sign{position:absolute;left:18px;top:236px}
.sign-name{font-size:6.5px;color:#444}
.sign-role{font-size:4px;color:var(--muted)}
.sign-script{font-family:'Great Vibes',cursive;font-size:14px;color:#5b5fa8;margin-top:3px}
.compliment{left:620px;top:905px;width:395px;height:197px}
</style>
</head>
<body>
<svg width="0" height="0" style="position:absolute" aria-hidden="true">
  <symbol id="i-phone" viewBox="0 0 10 10"><path d="M2 1l2 2-1 1.2c.6 1.2 1.6 2.2 2.8 2.8L7 6l2 2-1.2 1.4C4.5 9.2.8 5.5.6 2.2z"/></symbol>
  <symbol id="i-fax" viewBox="0 0 10 10"><rect x="1" y="4" width="8" height="5" rx="1"/><rect x="3" y="1" width="4" height="3"/></symbol>
  <symbol id="i-send" viewBox="0 0 10 10"><path d="M9.5.5L.5 4.5l3.5 1.2L5 9.5z"/></symbol>
  <symbol id="i-link" viewBox="0 0 10 10"><path d="M4 6L6 4M3.5 4.5L2 6a1.4 1.4 0 002 2l1.5-1.5M6.5 5.5L8 4a1.4 1.4 0 00-2-2L4.5 3.5" stroke="currentColor" fill="none" stroke-width="1.3" style="stroke:var(--blue)"/></symbol>
  <symbol id="i-pin" viewBox="0 0 10 10"><path d="M5 .5a3.3 3.3 0 00-3.3 3.3C1.7 6.5 5 9.5 5 9.5s3.3-3 3.3-5.7A3.3 3.3 0 005 .5zm0 4.7a1.4 1.4 0 110-2.8 1.4 1.4 0 010 2.8z"/></symbol>
</svg>

<!-- Presentation folder, outside -->
<section class="sheet folder-outside">
  <div class="folder-spine">
    <ul class="contact light" style="left:22px;top:243px;font-size:3.6px">
      <li><svg><use href="#i-phone"/></svg>555-010-2741</li>
      <li><svg><use href="#i-fax"/></svg>555-010-3386</li>
      <li><svg><use href="#i-send"/></svg>contact@brightkeelhomes.example</li>
      <li><svg><use href="#i-link"/></svg>www.brightkeelhomes.example</li>
      <li class="gap"><svg><use href="#i-pin"/></svg>420 Harbor Lane, Ste 110, Coral Bay, FL 30000</li>
    </ul>
  </div>
  <div class="brand" style="left:258px;top:180px;font-size:17px"><span class="brand-mark"></span>Brightkeel Homes</div>
  <div class="base-band" style="left:206px"></div>
</section>

<!-- Presentation folder, inside -->
<section class="sheet folder-inside">
  <svg class="folder-pocket" viewBox="0 0 413 292" preserveAspectRatio="none" aria-hidden="true">
    <path d="M206 292 L217 214 Q219 205 228 205 L413 205 L413 292 Z" fill="var(--grey)"/>
  </svg>
</section>

<!-- Large envelope -->
<section class="envelope" style="left:705px;top:79px;width:297px;height:469px">
  <svg class="body" viewBox="0 0 297 469" preserveAspectRatio="none" aria-hidden="true">
    <rect x="0" y="50" width="297" height="419" fill="var(--paper)" style="filter:drop-shadow(0 3px 3px rgba(0,0,0,.2))"/>
    <path d="M8 6 Q9 0 16 0 L280 0 Q286 0 287 6 L297 50 Q280 60 272 76 L16 76 Q8 60 0 50 Z" fill="var(--grey)"/>
    <rect x="0" y="49" width="297" height="28" fill="var(--grey-dark)" opacity=".5"/>
    <path d="M16 154 Q16 76 40 76 L258 76 Q282 76 282 154 Z" fill="var(--paper)"/>
    <path d="M12 469 L16 100 Q16 76 40 76 L258 76 Q282 76 282 100 L286 469" fill="none" stroke="#eee" stroke-width="1"/>
  </svg>
</section>

<!-- Business card -->
<section class="sheet card-front">
  <div class="brand on-grey" style="left:34px;top:36px;font-size:7.5px"><span class="brand-mark"></span>Brightkeel Homes</div>
</section>
<section class="sheet card-back">
  <div class="card-name">YOUR NAME</div>
  <div class="card-role">Designation</div>
  <ul class="contact" style="left:14px;top:34px;font-size:3.2px">
    <li><svg><use href="#i-phone"/></svg>555-010-2741</li>
    <li><svg><use href="#i-fax"/></svg>555-010-3386</li>
    <li><svg><use href="#i-send"/></svg>contact@brightkeelhomes.example</li>
    <li><svg><use href="#i-link"/></svg>www.brightkeelhomes.example</li>
    <li class="gap"><svg><use href="#i-pin"/></svg>420 Harbor Lane, Ste 110,<br>Coral Bay, FL 30000</li>
  </ul>
  <div class="base-band"></div>
</section>

<!-- Tall letterhead -->
<section class="sheet letter-tall">
  <div class="brand" style="left:28px;top:80px;font-size:10px"><span class="brand-mark"></span>Brightkeel Homes</div>
  <ul class="contact" style="left:178px;top:38px;font-size:6.6px">
    <li><svg><use href="#i-phone"/></svg>555-010-2741</li>
    <li><svg><use href="#i-fax"/></svg>555-010-3386</li>
    <li><svg><use href="#i-send"/></svg>contact@brightkeelhomes.example</li>
    <li><svg><use href="#i-link"/></svg>www.brightkeelhomes.example</li>
    <li class="gap"><svg><use href="#i-pin"/></svg>420 Harbor Lane, Ste 110,<br>Coral Bay, FL 30000</li>
  </ul>
  <div class="base-band"></div>
</section>

<!-- Letter -->
<section class="sheet letter">
  <div class="brand" style="left:18px;top:62px;font-size:8px"><span class="brand-mark"></span>Brightkeel Homes</div>
  <ul class="contact" style="left:197px;top:35px;font-size:4.4px">
    <li><svg><use href="#i-phone"/></svg>555-010-2741</li>
    <li><svg><use href="#i-fax"/></svg>555-010-3386</li>
    <li><svg><use href="#i-send"/></svg>contact@brightkeelhomes.example</li>
    <li><svg><use href="#i-link"/></svg>www.brightkeelhomes.example</li>
    <li class="gap"><svg><use href="#i-pin"/></svg>420 Harbor Lane, Ste 110,<br>Coral Bay, FL 30000</li>
  </ul>
  <div class="letter-body" style="top:115px">
    <div class="letter-head"><span>Dear, Mr___________</span><span>Date : 14.06.2019</span></div>
    <p>Lorem Ipsum is simply dummy text of the printing and typesetting industry. Lorem Ipsum has been the industry's standard dummy text ever since the1500s,when an unknown printer took a galley of type and scrambled it to make a type specimen book. It has survived not only five centuries, but also the leap into electronic typesetting, remaining essentially unchanged.</p>
    <p>Lorem Ipsum is simply dummy text of the printing and typesetting industry. Lorem Ipsum has been the industry's standard dummy text ever since the1500s.</p>
    <p>Lorem Ipsum is simply dummy text of the printing and typesetting industry.</p>
  </div>
  <div class="letter-sign">
    <div class="sign-name">Your Name</div>
    <div class="sign-role">Designation</div>
    <div class="sign-script">Signature</div>
  </div>
  <div class="base-band"></div>
</section>

<!-- Small envelope -->
<section class="envelope" style="left:551px;top:761px;width:395px;height:262px">
  <svg class="body" viewBox="0 0 395 262" preserveAspectRatio="none" aria-hidden="true">
    <rect x="0" y="65" width="395" height="197" fill="var(--paper)" style="filter:drop-shadow(0 3px 3px rgba(0,0,0,.2))"/>
    <path d="M8 10 Q10 0 22 0 L370 0 Q382 0 384 10 L395 65 Q375 75 368 98 L20 98 Q12 75 0 65 Z" fill="var(--grey)"/>
    <rect x="0" y="65" width="395" height="34" fill="var(--grey-dark)" opacity=".5"/>
    <path d="M12 150 L16 118 Q18 98 40 98 L354 98 Q376 98 378 118 L382 150 Z" fill="var(--paper)"/>
  </svg>
</section>

<!-- Compliment slip -->
<section class="sheet compliment">
  <div class="brand" style="left:35px;top:72px;font-size:10px"><span class="brand-mark"></span>Brightkeel Homes</div>
  <ul class="contact" style="left:35px;top:116px;font-size:6.3px">
    <li><svg><use href="#i-phone"/></svg>555-010-2741</li>
    <li><svg><use href="#i-fax"/></svg>555-010-3386</li>
    <li><svg><use href="#i-send"/></svg>contact@brightkeelhomes.example</li>
    <li><svg><use href="#i-link"/></svg>www.brightkeelhomes.example</li>
    <li class="gap"><svg><use href="#i-pin"/></svg>420 Harbor Lane, Ste 110, Coral Bay, FL 30000</li>
  </ul>
  <div class="base-band" style="height:5px"></div>
</section>
</body>
</html>
```